Letterhead and Stationary for Construction Company

Brisk Current needs modern Letterhead, Envelopes and Notepad designs.

Industry/Entity Type

Construction

Colors
f78f20
34a7d8
ffffff

Requirements
Must have
• Modern looking design.

```html
<!DOCTYPE html>
<html lang="en">
<head>
<meta charset="utf-8">
<title>Brisk Current Letterhead</title>
<link rel="stylesheet" href="https://fonts.googleapis.com/css2?family=Nunito:wght@700&family=Open+Sans:wght@400&display=swap">
<style>
  :root {
    --orange: #e57a35;
    --blue: #3a78b8;
    --ink: #3b3d40;
    --paper: #ffffff;
  }
  * { margin: 0; padding: 0; box-sizing: border-box; }
  html, body {
    width: 1066px;
    height: 1200px;
    overflow: hidden;
    background: var(--paper);
  }
  .letterhead {
    position: relative;
    width: 1066px;
    height: 1200px;
    background: var(--paper);
    font-family: "Open Sans", Arial, sans-serif;
    color: var(--ink);
  }
  .brand {
    position: absolute;
    left: 110px;
    top: 78px;
    display: flex;
    align-items: center;
    gap: 12px;
  }
  .brand-dot {
    width: 34px;
    height: 34px;
    border-radius: 50%;
    background: var(--orange);
  }
  .brand-name {
    font-family: "Nunito", Arial, sans-serif;
    font-weight: 700;
    font-size: 34px;
    line-height: 1;
    color: var(--blue);
    letter-spacing: -0.5px;
  }
  .contact {
    position: absolute;
    top: 86px;
    right: 72px;
    display: flex;
    gap: 18px;
    font-size: 13.5px;
    line-height: 20px;
  }
  .contact-address { white-space: nowrap; }
  .contact-lines { list-style: none; }
  .contact-lines li {
    display: flex;
    align-items: center;
    gap: 8px;
    white-space: nowrap;
  }
  .contact-icon {
    width: 11px;
    height: 11px;
    fill: var(--blue);
    flex: none;
  }
  .footer-stripes {
    position: absolute;
    left: 0;
    right: 0;
    bottom: 18px;
  }
  .stripe { height: 11px; }
  .stripe-orange { background: var(--orange); }
  .stripe-gap { height: 6px; background: var(--paper); }
  .stripe-blue { background: var(--blue); }
</style>
</head>
<body>
  <main class="letterhead">
    <header>
      <div class="brand">
        <span class="brand-dot"></span>
        <span class="brand-name">Brisk Current</span>
      </div>
      <div class="contact">
        <address class="contact-address" style="font-style:normal">
          42 Foundry Lane, Mill Road<br>
          North yard side<br>
          CA 730415
        </address>
        <ul class="contact-lines">
          <li>
            <svg class="contact-icon" viewBox="0 0 12 12" aria-hidden="true"><path d="M2.5 1 4.5 1 5.3 3.6 4 4.6C4.7 6 6 7.3 7.4 8L8.4 6.7 11 7.5 11 9.5C11 10.3 10.3 11 9.5 11 4.8 11 1 7.2 1 2.5 1 1.7 1.7 1 2.5 1Z"/></svg>
            +555 0142 3867
          </li>
          <li>
            <svg class="contact-icon" viewBox="0 0 12 12" aria-hidden="true"><path d="M1 3h10v7H1z M1 3l5 4 5-4" fill="none" stroke="#3a78b8" stroke-width="1.6"/></svg>
            hello@briskcurrent.com
          </li>
          <li>
            <svg class="contact-icon" viewBox="0 0 12 12" aria-hidden="true"><circle cx="6" cy="6" r="5" fill="none" stroke="#3a78b8" stroke-width="1.4"/><path d="M1 6h10M6 1c-2.5 3-2.5 7 0 10M6 1c2.5 3 2.5 7 0 10" fill="none" stroke="#3a78b8" stroke-width="1"/></svg>
            www.briskcurrent.com
          </li>
        </ul>
      </div>
    </header>
    <footer class="footer-stripes">
      <div class="stripe stripe-orange"></div>
      <div class="stripe-gap"></div>
      <div class="stripe stripe-blue"></div>
    </footer>
  </main>
</body>
</html>
```